Business card design

I need my logo on this card, things I need the card to have on it
licensed and insured.
owner operators Derek & Milton Halvorsen
my phone number 5418237906
Disaster Recovery, Storm Damage Restoration, Proactive Disaster Plan Management, Roof Repair/Restoration Structural Repair and Reconstruction, Emergency Boarding and Tarping Service, Perimeter Fencing, Emergency Tree Removal,

```html
<!DOCTYPE html>
<html lang="en">
<head>
<meta charset="utf-8">
<title>Halvorsen Construction – Business Card</title>
<link rel="stylesheet" href="https://fonts.googleapis.com/css2?family=Lato:wght@300;400;700;900&display=swap">
<style>
  :root {
    --stage: #3a3a3a;
    --card-dark: #1d1d1d;
    --brand-blue: #1596e6;
    --text-light: #e9e9e9;
    --white: #ffffff;
  }
  * { box-sizing: border-box; margin: 0; padding: 0; }
  html, body {
    width: 1200px; height: 875px; overflow: hidden;
    background: var(--stage);
    font-family: "Lato", sans-serif;
  }
  .canvas {
    position: relative; width: 1200px; height: 875px;
    display: flex; align-items: center; justify-content: center; gap: 50px;
  }
  .card {
    position: relative; width: 540px; height: 309px;
    border-radius: 16px; overflow: hidden;
  }

  /* Back: services */
  .card--services { background: var(--card-dark); display: flex; align-items: center; }
  .brand {
    width: 230px; padding-left: 30px;
    display: flex; flex-direction: column; align-items: flex-start;
  }
  .brand__row { display: flex; align-items: center; gap: 10px; }
  .brand__square { width: 18px; height: 18px; background: var(--brand-blue); }
  .brand__name {
    color: var(--brand-blue); font-weight: 400; font-size: 30px; letter-spacing: 0.5px;
  }
  .brand__sub {
    color: var(--brand-blue); font-weight: 400; font-size: 9.5px;
    letter-spacing: 5px; margin-top: 4px; padding-left: 28px;
  }
  .divider { width: 2px; height: 170px; background: var(--brand-blue); margin: 0 22px 0 6px; }
  .services { list-style: none; display: flex; flex-direction: column; gap: 5px; }
  .services li {
    display: flex; align-items: center; gap: 9px;
    color: var(--text-light); font-size: 12.5px; font-weight: 400;
  }
  .tick { width: 13px; height: 13px; flex: none; }

  /* Front: contact */
  .card--contact { background: var(--brand-blue); color: var(--white); }
  .contact { position: absolute; left: 36px; bottom: 34px; }
  .contact__names {
    font-weight: 900; font-size: 30px; line-height: 1.05; text-transform: uppercase;
  }
  .contact__role { font-weight: 300; font-size: 17px; margin-top: 2px; }
  .rule { width: 30px; height: 2px; background: var(--white); margin: 12px 0 8px; }
  .contact__cta { font-weight: 700; font-size: 15px; }
  .contact__phone { font-weight: 900; font-size: 32px; line-height: 1.05; letter-spacing: 0.5px; }
  .contact__note { font-weight: 700; font-size: 15px; }
  .mark-square {
    position: absolute; right: 60px; top: 70px; width: 110px; height: 110px;
    background: var(--white);
  }
</style>
</head>
<body>
<main class="canvas">

  <section class="card card--services" aria-label="Services side">
    <div class="brand">
      <div class="brand__row">
        <span class="brand__square"></span>
        <span class="brand__name">HALVORSEN</span>
      </div>
      <span class="brand__sub">CONSTRUCTION L.L.C</span>
    </div>
    <span class="divider"></span>
    <ul class="services">
      <li><svg class="tick" viewBox="0 0 14 14"><circle cx="7" cy="7" r="7" fill="#1596e6"/><path d="M4 7.2l2 2 4-4.2" stroke="#1d1d1d" stroke-width="1.8" fill="none"/></svg>Disaster Recovery</li>
      <li><svg class="tick" viewBox="0 0 14 14"><circle cx="7" cy="7" r="7" fill="#1596e6"/><path d="M4 7.2l2 2 4-4.2" stroke="#1d1d1d" stroke-width="1.8" fill="none"/></svg>Storm Damage Restoration</li>
      <li><svg class="tick" viewBox="0 0 14 14"><circle cx="7" cy="7" r="7" fill="#1596e6"/><path d="M4 7.2l2 2 4-4.2" stroke="#1d1d1d" stroke-width="1.8" fill="none"/></svg>Proactive Disaster Plan Management</li>
      <li><svg class="tick" viewBox="0 0 14 14"><circle cx="7" cy="7" r="7" fill="#1596e6"/><path d="M4 7.2l2 2 4-4.2" stroke="#1d1d1d" stroke-width="1.8" fill="none"/></svg>Roof Repair / Restoration</li>
      <li><svg class="tick" viewBox="0 0 14 14"><circle cx="7" cy="7" r="7" fill="#1596e6"/><path d="M4 7.2l2 2 4-4.2" stroke="#1d1d1d" stroke-width="1.8" fill="none"/></svg>Structural Repair &amp; Reconstruction</li>
      <li><svg class="tick" viewBox="0 0 14 14"><circle cx="7" cy="7" r="7" fill="#1596e6"/><path d="M4 7.2l2 2 4-4.2" stroke="#1d1d1d" stroke-width="1.8" fill="none"/></svg>Emergency Boarding &amp; Tarping Service</li>
      <li><svg class="tick" viewBox="0 0 14 14"><circle cx="7" cy="7" r="7" fill="#1596e6"/><path d="M4 7.2l2 2 4-4.2" stroke="#1d1d1d" stroke-width="1.8" fill="none"/></svg>Perimeter Fencing</li>
      <li><svg class="tick" viewBox="0 0 14 14"><circle cx="7" cy="7" r="7" fill="#1596e6"/><path d="M4 7.2l2 2 4-4.2" stroke="#1d1d1d" stroke-width="1.8" fill="none"/></svg>Emergency Tree Removal</li>
    </ul>
  </section>

  <section class="card card--contact" aria-label="Contact side">
    <span class="mark-square"></span>
    <div class="contact">
      <p class="contact__names">Derek &amp;<br>Milton<br>Halvorsen</p>
      <p class="contact__role">Owner Operators</p>
      <span class="rule"></span>
      <p class="contact__cta">Call Us Today</p>
      <p class="contact__phone">5418237906</p>
      <span class="rule"></span>
      <p class="contact__note">licensed &amp; insured</p>
    </div>
  </section>

</main>
</body>
</html>
```